Business Card Design Project

Please create a custom business card for Birchmoor Links School. The logo is attached to this brief.

Colours could be based on Blue, black, red, or white color. Colors like orange, green, purple, pink are not preferable.

Here is the link to the logo project : http://tasks.artquarrel.net/task.aspx?id=413057

Questions can be posted on the Discussion Board.

```html
<!DOCTYPE html>
<html lang="en">
<head>
<meta charset="utf-8">
<title>Birchmoor Links School – Business Card</title>
<link rel="stylesheet" href="https://fonts.googleapis.com/css2?family=Open+Sans:wght@400;600;700&display=swap">
<style>
  :root {
    --navy: #0f2a78;
    --navy-deep: #0a1f5e;
    --ink: #1d1d1f;
    --charcoal: #2f2f33;
    --paper: #ffffff;
    --backdrop: #d9d9d6;
  }
  * { box-sizing: border-box; margin: 0; padding: 0; }
  html, body { width: 1200px; height: 871px; overflow: hidden; }
  body {
    background: var(--backdrop);
    font-family: "Open Sans", Arial, sans-serif;
    position: relative;
  }
  .card {
    position: absolute;
    width: 540px;
    height: 310px;
    overflow: hidden;
    box-shadow: 0 8px 22px rgba(0,0,0,0.25);
  }
  .card--back {
    left: 50px; top: 110px;
    background: linear-gradient(160deg, #17388f 0%, var(--navy) 55%, var(--navy-deep) 100%);
    display: flex; align-items: center; justify-content: center;
  }
  .card--front { left: 610px; top: 450px; background: var(--paper); }

  .brand { display: flex; align-items: center; gap: 12px; }
  .brand__dot { width: 34px; height: 34px; border-radius: 50%; flex: none; }
  .brand__name { font-weight: 700; line-height: 1.1; }
  .card--back .brand__dot { background: var(--paper); }
  .card--back .brand__name { color: var(--paper); font-size: 26px; }

  .card--front .brand { position: absolute; left: 36px; top: 92px; }
  .card--front .brand__dot { background: var(--navy); }
  .card--front .brand__name { color: var(--navy); font-size: 20px; width: 170px; }

  .wave { position: absolute; left: 0; top: 0; width: 540px; height: 310px; }

  .contact { position: absolute; left: 302px; top: 64px; color: var(--ink); }
  .contact__name { font-weight: 700; font-size: 17px; letter-spacing: 1px; }
  .contact__role { color: var(--navy); font-size: 13px; letter-spacing: 0.5px; margin-bottom: 16px; }
  .contact__address { font-size: 12.5px; line-height: 1.5; letter-spacing: 0.4px; margin-bottom: 12px; }
  .contact__list { list-style: none; font-size: 12.5px; letter-spacing: 0.4px; }
  .contact__list li { display: flex; align-items: center; height: 21px; }
  .contact__icon { width: 12px; height: 12px; margin-right: 14px; flex: none; fill: var(--navy); }
</style>
</head>
<body>

<section class="card card--back" aria-label="Card back">
  <div class="brand">
    <span class="brand__dot"></span>
    <span class="brand__name">Birchmoor Links School</span>
  </div>
</section>

<section class="card card--front" aria-label="Card front">
  <svg class="wave" viewBox="0 0 540 310" aria-hidden="true">
    <path d="M0,205 C160,188 320,235 540,308 L540,310 L0,310 Z" fill="var(--navy)"/>
    <path d="M0,193 C160,174 330,220 540,302" fill="none" stroke="var(--charcoal)" stroke-width="7"/>
  </svg>

  <div class="brand">
    <span class="brand__dot"></span>
    <span class="brand__name">Birchmoor Links School</span>
  </div>

  <div class="contact">
    <p class="contact__name">Dale Harwick</p>
    <p class="contact__role">President</p>
    <p class="contact__address">PO Box 218<br>Ashcombe Falls, RI 02914</p>
    <ul class="contact__list">
      <li>
        <svg class="contact__icon" viewBox="0 0 12 12" aria-hidden="true"><path d="M1,4 Q6,0 11,4 L9,5.5 L8,4.5 L4,4.5 L3,5.5 Z M3,6 L9,6 L10.5,11 L1.5,11 Z"/></svg>
        +49 (0) 151 47203158
      </li>
      <li>
        <svg class="contact__icon" viewBox="0 0 12 12" aria-hidden="true"><path d="M0,2 L12,2 L12,10 L0,10 Z M1,3 L6,7 L11,3" stroke="#fff" stroke-width="0.8"/></svg>
        dale@birchmoorlinks.com
      </li>
      <li>
        <svg class="contact__icon" viewBox="0 0 12 12" aria-hidden="true"><circle cx="6" cy="6" r="5.5"/><path d="M0.5,6 H11.5 M6,0.5 V11.5 M6,0.5 C3,3 3,9 6,11.5 M6,0.5 C9,3 9,9 6,11.5" stroke="#fff" stroke-width="0.7" fill="none"/></svg>
        www.birchmoorlinks.com
      </li>
    </ul>
  </div>
</section>

</body>
</html>
```